I need a great, modern, professional website for my paint contracting company, Brookhollow Paint Contractors, LLC. I have many good pix that can be used from jobs completed that would be attractive. We do commercial, residential and industrial jobs. I’m fully insured and licensed, including holding a General Contractor’s License as a Subcontractor. I know nothing about coding websites. I’ll have my assistant get on tomorrow and learn how to drop files. I’m not sure what files to send. This will be difficult at best, it being able to talk this through. Oh well. What’s next?

Target Market(s)

General Contractors

Industry/Entity Type

Paint Contracting

Coding

Coded - Design and coding required

Font styles to use
Sans Serif

Colors
00AB8E
00BBA5
67D7C9
C6EFE9
E9F9F6

Requirements
Must have
• Pix of completed jobs, bio, maybe testimonials from happy customers? ….
Nice to have
• I’d like it to have a modern appeal, but still have some warmth.
Should not have
• ??

```html
<!DOCTYPE html>
<html lang="en">
<head>
<meta charset="utf-8">
<title>Brookhollow Paint Contractors, LLC</title>
<link href="https://fonts.googleapis.com/css2?family=Poppins:wght@500;600;700&family=Roboto:wght@400;500;700&display=swap" rel="stylesheet">
<style>
:root{
  --green:#00AB8E;
  --teal:#00BBA5;
  --mint:#67D7C9;
  --pale:#C6EFE9;
  --wash:#E9F9F6;
  --ink:#1d1d1d;
  --text:#555;
  --footer:#101212;
  --white:#fff;
  --star:#f5b800;
}
*{margin:0;padding:0;box-sizing:border-box}
html,body{width:1200px;height:4491px;overflow:hidden}
body{position:relative;font-family:'Roboto',sans-serif;color:var(--ink);background:var(--white)}
.abs{position:absolute}
h1,h2,h3,.display{font-family:'Poppins',sans-serif}

/* header */
.site-header{position:absolute;left:0;top:0;width:1200px;height:105px;background:var(--white)}
.brand{position:absolute;left:48px;top:18px;font-family:'Poppins',sans-serif;font-weight:700;font-size:29px;line-height:35px;color:var(--ink)}
.socials{position:absolute;left:560px;top:18px;display:flex;gap:12px}
.socials span{width:29px;height:29px;border:1.5px solid var(--green);border-radius:50%}
.quote-btn{position:absolute;left:748px;top:14px;width:136px;height:38px;background:var(--green);color:#fff;border-radius:3px;font-size:13px;font-weight:500;display:flex;align-items:center;justify-content:center;gap:8px}
.nav-bar{position:absolute;left:322px;top:65px;width:640px;height:40px;background:var(--green);clip-path:polygon(30px 0,100% 0,100% 100%,0 100%)}
.nav-bar ul{list-style:none;display:flex;gap:28px;position:absolute;left:56px;top:11px;font-size:13px;color:#dff5f0}
.nav-bar li.active{color:#fff;font-weight:700}
.call-box{position:absolute;left:942px;top:0;width:258px;height:105px;background:var(--green);clip-path:polygon(20px 0,100% 0,100% 100%,0 100%)}
.call-icon{position:absolute;left:30px;top:36px;width:38px;height:38px;border-radius:50%;border:2px solid rgba(255,255,255,.6);display:flex;align-items:center;justify-content:center}
.call-label{position:absolute;left:86px;top:31px;color:#fff;font-size:12px}
.call-number{position:absolute;left:86px;top:52px;color:#fff;font-size:20px;font-weight:700}

/* hero */
.hero{position:absolute;left:0;top:105px;width:1200px;height:603px;background:linear-gradient(90deg,#eef1f3 0%,#e9d9dc 40%,#d98e9b 70%,#c8cfd6 100%)}
.hero-photo{position:absolute;inset:0}
.hero-welcome{position:absolute;left:108px;top:178px;font-family:'Poppins',sans-serif;font-weight:600;font-size:27px;color:var(--green)}
.hero-title{position:absolute;left:108px;top:222px;font-size:47px;line-height:46px;font-weight:700;color:#222}
.hero-text{position:absolute;left:108px;top:332px;width:370px;font-size:14.5px;line-height:26px;color:#222}
.btn-solid{position:absolute;height:47px;background:var(--green);color:#fff;border-radius:3px;font-size:14px;font-weight:700;display:flex;align-items:center;justify-content:center;gap:10px;letter-spacing:.3px}

/* about */
.about{position:absolute;left:0;top:708px;width:1200px;height:626px;background:var(--white)}
.about-hex{position:absolute;left:113px;top:85px;width:394px;height:454px}
.rule{height:4px;background:var(--green);border-radius:2px}
.about-title{position:absolute;left:598px;top:166px;font-size:35px;line-height:41px;font-weight:700;color:#1d1d1d}
.about-text{position:absolute;left:598px;top:264px;width:486px;font-size:15px;line-height:25px;color:var(--text);text-align:justify}
.btn-outline{position:absolute;left:598px;top:452px;width:157px;height:44px;border:2px solid var(--green);border-radius:4px;color:var(--green);font-size:13.5px;font-weight:700;display:flex;align-items:center;justify-content:center;gap:8px}

/* section titles */
.section-title{position:absolute;left:0;width:1200px;text-align:center;font-size:35px;font-weight:700}
.title-rule{position:absolute;left:555px;width:90px;height:4px;background:var(--green);border-radius:2px}

/* services */
.services{position:absolute;left:0;top:1334px;width:1200px;height:644px;background:linear-gradient(135deg,var(--pale),var(--wash) 55%,var(--pale))}
.service-card{position:absolute;top:157px;width:323px;height:407px}
.service-photo{position:absolute;left:0;top:0;width:323px;height:236px;border-radius:4px 4px 0 0}
.service-body{position:absolute;left:9px;top:180px;width:305px;height:227px;background:#fff;border-radius:6px;box-shadow:0 4px 14px rgba(0,0,0,.08)}
.service-body::before{content:"";position:absolute;left:0;top:-36px;width:305px;height:72px;background:#fff;border-radius:50% 50% 0 0 / 100% 100% 0 0;border-top:3px solid var(--green)}
.service-icon{position:absolute;left:127px;top:-40px;width:52px;height:52px;border-radius:50%;background:#fff;display:flex;align-items:center;justify-content:center;z-index:2}
.service-name{position:absolute;left:0;top:30px;width:100%;text-align:center;font-family:'Roboto',sans-serif;font-weight:700;font-size:16px;z-index:2}
.service-text{position:absolute;left:20px;top:75px;width:265px;text-align:center;font-size:15px;line-height:26px;color:var(--text)}
.service-link{position:absolute;left:0;top:178px;width:100%;display:flex;justify-content:center;gap:10px;color:var(--green);font-size:14px;font-weight:700}

/* insured band */
.licensed{position:absolute;left:0;top:1978px;width:1200px;height:272px;background:linear-gradient(90deg,#0d9a7f,var(--green) 50%,#0d9a7f)}
.licensed p{position:absolute;left:0;top:56px;width:1200px;text-align:center;font-family:'Poppins',sans-serif;font-weight:600;font-size:35px;line-height:49px;color:#fff}

/* gallery */
.gallery{position:absolute;left:0;top:2250px;width:1200px;height:814px;background:#fff}
.gallery-item{position:absolute}

/* team */
.team{position:absolute;left:0;top:3064px;width:1200px;height:541px;background:linear-gradient(90deg,#14a88b,#1ab198 50%,#14a88b)}
.member{position:absolute;top:197px;width:260px;text-align:center;color:#fff}
.member-photo{margin:0 auto;width:164px;height:164px;border-radius:50%;border:3px solid #fff;padding:5px}
.member-photo div{width:100%;height:100%;border-radius:50%}
.member-name{margin-top:25px;font-family:'Poppins',sans-serif;font-weight:600;font-size:16px}
.member-bio{margin-top:12px;font-size:14px;line-height:24px;color:#e5faf5}

/* testimonials */
.testimonials{position:absolute;left:0;top:3605px;width:1200px;height:497px;background:linear-gradient(180deg,#f6f7f7,#fbfbfb)}
.review{position:absolute;top:173px;width:423px;height:207px;background:#fff;box-shadow:0 3px 16px rgba(0,0,0,.07)}
.stars{position:absolute;left:20px;top:18px;color:var(--star);font-size:15px;letter-spacing:4px}
.review-text{position:absolute;left:20px;top:52px;width:383px;font-size:15px;line-height:26px;color:var(--text);text-align:justify}
.review-name{position:absolute;left:20px;top:140px;font-weight:700;font-size:15px}
.review-quote{position:absolute;right:16px;top:145px;font-family:'Poppins',sans-serif;font-size:90px;line-height:90px;color:#e4e6e6;font-weight:700}
.review-avatar{position:absolute;left:17px;top:170px;width:72px;height:72px;border-radius:50%;background:linear-gradient(135deg,#6b6f73,#3b3f44);border:3px solid #fff}

/* footer */
.site-footer{position:absolute;left:0;top:4102px;width:1200px;height:389px;background:var(--footer);color:#fff}
.footer-col{position:absolute;top:62px}
.footer-col h4{font-family:'Roboto',sans-serif;font-size:15px;font-weight:700;margin-bottom:26px}
.footer-col ul{list-style:none;font-size:13px;line-height:26px;color:#e6e6e6}
.contact-item{display:flex;gap:10px;font-size:12.5px;line-height:17px;color:#e6e6e6;margin-bottom:16px}
.contact-item b{display:block;font-size:11.5px;color:#fff}
.footer-note{font-size:12px;line-height:19px;color:#e6e6e6;width:235px}
.footer-btn{margin-top:26px;width:193px;height:43px;background:var(--green);border-radius:3px;display:flex;align-items:center;justify-content:center;font-size:14px;font-weight:500}
.to-top{position:absolute;left:1110px;top:290px;width:34px;height:34px;border-radius:50%;background:var(--green);display:flex;align-items:center;justify-content:center}
.copyright{position:absolute;left:0;top:348px;width:1200px;text-align:center;font-size:13px;color:#eee}
</style>
</head>
<body>

<header class="site-header">
  <div class="brand">Brookhollow Paint<br>Contractors, LLC</div>
  <div class="socials"><span></span><span></span><span></span><span></span></div>
  <div class="quote-btn">GET A QUOTE
    <svg width="12" height="12" viewBox="0 0 12 12"><circle cx="6" cy="6" r="6" fill="#fff"/><path d="M5 3.5 7.5 6 5 8.5" stroke="var(--green)" stroke-width="1.6" fill="none"/></svg>
  </div>
  <nav class="nav-bar">
    <ul><li class="active">Home</li><li>About Us</li><li>Services</li><li>Gallery</li><li>TeamTestimonoals</li><li>Contact Us</li></ul>
  </nav>
  <div class="call-box">
    <div class="call-icon"><svg width="18" height="18" viewBox="0 0 24 24"><path d="M6.6 10.8a15 15 0 0 0 6.6 6.6l2.2-2.2a1 1 0 0 1 1-.25 11.4 11.4 0 0 0 3.6.57 1 1 0 0 1 1 1V20a1 1 0 0 1-1 1A17 17 0 0 1 3 4a1 1 0 0 1 1-1h3.5a1 1 0 0 1 1 1c0 1.25.2 2.45.57 3.57a1 1 0 0 1-.25 1z" fill="#fff"/></svg></div>
    <div class="call-label">Call Us Today</div>
    <div class="call-number">+1 555 014 2270</div>
  </div>
</header>

<section class="hero">
  <div class="hero-photo" role="img" aria-label="Painter pouring red paint into a tray while a colleague rolls orange paint on a pink wall"></div>
  <div class="hero-welcome">Welcome to</div>
  <h1 class="hero-title">Brookhollow Paint<br>Contractors</h1>
  <p class="hero-text">Lorem ipsum dolor sit ame, consectetur adipiscing iusm tempor incididunt ut labore et dolore magna.</p>
  <div class="btn-solid" style="left:108px;top:406px;width:154px">GET STARTED
    <svg width="13" height="13" viewBox="0 0 12 12"><circle cx="6" cy="6" r="6" fill="#fff"/><path d="M5 3.5 7.5 6 5 8.5" stroke="var(--green)" stroke-width="1.6" fill="none"/></svg>
  </div>
</section>

<section class="about">
  <svg class="about-hex" viewBox="0 0 394 454">
    <polygon points="197,4 390,115 390,339 197,450 4,339 4,115" fill="#fff" stroke="#e1e1e1" stroke-width="3"/>
    <polygon points="197,16 379,121 379,333 197,438 15,333 15,121" fill="url(#hexfill)" role="img" aria-label="Painter in harness rolling yellow paint on a building facade"/>
    <defs><linearGradient id="hexfill" x1="0" y1="0" x2="1" y2="1"><stop offset="0" stop-color="#8d8f86"/><stop offset=".55" stop-color="#c9b06a"/><stop offset="1" stop-color="#6d665a"/></linearGradient></defs>
  </svg>
  <div class="rule abs" style="left:598px;top:141px;width:56px"></div>
  <h2 class="about-title">About Brookhollow Paint<br>Contractors</h2>
  <p class="about-text">Lorem ipsum dolor sit amet, consectetur adipiscing elit sed eiusmod tempor incididunt ut labore et dolore magna aliqua Ut enim ad minim veniam, quis nostrud exercitation ullamco laboris nisi ut aliquip ex ea commodo consequat. Duis aute irure dolor in reprehenderit in voluptate velit esse cillum dolore eu fugiat nulla pariatur. ExcepteLorem ipsum dolor sit amet, consectetur adipiscing elit, sed do eiusmod tempor incididunt ut labore et dolore magna aliqua. Ut enim ad minim</p>
  <div class="btn-outline">LEARN MORE
    <svg width="13" height="13" viewBox="0 0 12 12"><circle cx="6" cy="6" r="6" fill="var(--green)"/><path d="M5 3.5 7.5 6 5 8.5" stroke="#fff" stroke-width="1.6" fill="none"/></svg>
  </div>
</section>

<section class="services">
  <h2 class="section-title" style="top:52px">Our Services</h2>
  <div class="title-rule" style="top:109px"></div>

  <article class="service-card" style="left:96px">
    <div class="service-photo" role="img" aria-label="Two painters in hi-vis vests working on a ceiling" style="background:linear-gradient(160deg,#e6e3dc,#b8ab8d 60%,#8e8a7a)"></div>
    <div class="service-body">
      <div class="service-icon"><svg width="34" height="34" viewBox="0 0 34 34" fill="none" stroke="var(--green)" stroke-width="1.8"><rect x="6" y="8" width="12" height="22"/><rect x="18" y="14" width="10" height="16"/><path d="M9 12h2M13 12h2M9 17h2M13 17h2M9 22h2M13 22h2M21 18h4M21 23h4M4 30h26"/></svg></div>
      <h3 class="service-name">Commercial</h3>
      <p class="service-text">Lorem ipsum dolor amet consectetur adipiscinsed eiusmoded incididunted labored dolore magna aliquad.</p>
      <div class="service-link">LEARN MOR <svg width="13" height="13" viewBox="0 0 12 12"><circle cx="6" cy="6" r="6" fill="var(--green)"/><path d="M5 3.5 7.5 6 5 8.5" stroke="#fff" stroke-width="1.6" fill="none"/></svg></div>
    </div>
  </article>

  <article class="service-card" style="left:440px">
    <div class="service-photo" role="img" aria-label="Smiling woman painting a wall with a blue roller" style="background:linear-gradient(160deg,#dfe4ea,#b9c3cf 50%,#2f5ea8)"></div>
    <div class="service-body">
      <div class="service-icon"><svg width="34" height="34" viewBox="0 0 34 34" fill="none" stroke="var(--green)" stroke-width="1.8"><path d="M5 15 17 5l12 10M8 13v10h18V13"/><rect x="13" y="15" width="8" height="5"/><path d="M17 20v4M15 24h4v6h-4z"/></svg></div>
      <h3 class="service-name">Residential</h3>
      <p class="service-text">Lorem ipsum dolor amet consectetur adipiscinsed eiusmoded incididunted labored dolore magna aliquad.</p>
      <div class="service-link">LEARN MOR <svg width="13" height="13" viewBox="0 0 12 12"><circle cx="6" cy="6" r="6" fill="var(--green)"/><path d="M5 3.5 7.5 6 5 8.5" stroke="#fff" stroke-width="1.6" fill="none"/></svg></div>
    </div>
  </article>

  <article class="service-card" style="left:781px">
    <div class="service-photo" role="img" aria-label="Worker spray painting blue steel panels in an industrial yard" style="background:linear-gradient(160deg,#7d8a8c,#3d5aa6 55%,#1f3f9a)"></div>
    <div class="service-body">
      <div class="service-icon"><svg width="34" height="34" viewBox="0 0 34 34" fill="none" stroke="var(--green)" stroke-width="1.8"><path d="M5 30V14l7 4v-4l7 4v-4l7 4v12z"/><circle cx="24" cy="8" r="4"/><path d="M24 2v2M24 12v2M18 8h2M28 8h2M9 24h3M15 24h3M21 24h3"/></svg></div>
      <h3 class="service-name">Industrial jobs</h3>
      <p class="service-text">Lorem ipsum dolor amet consectetur adipiscinsed eiusmoded incididunted labored dolore magna aliquad.</p>
      <div class="service-link">LEARN MOR <svg width="13" height="13" viewBox="0 0 12 12"><circle cx="6" cy="6" r="6" fill="var(--green)"/><path d="M5 3.5 7.5 6 5 8.5" stroke="#fff" stroke-width="1.6" fill="none"/></svg></div>
    </div>
  </article>
</section>

<section class="licensed">
  <p>we are fully insured and licensed,<br>including holding a General Contractor’s<br>License as a Subcontractor.</p>
</section>

<section class="gallery">
  <h2 class="section-title" style="top:88px">Our Gallery</h2>
  <div class="title-rule" style="top:144px"></div>
  <div class="gallery-item" role="img" aria-label="Painter in safety glasses painting a window frame" style="left:112px;top:186px;width:483px;height:279px;background:linear-gradient(135deg,#c9a67a,#9fb8cf 50%,#2d64b8)"></div>
  <div class="gallery-item" role="img" aria-label="Painters in white coveralls painting an exterior wall" style="left:603px;top:186px;width:485px;height:279px;background:linear-gradient(135deg,#8f8b7d,#cfc8b5 45%,#7a8c6a)"></div>
  <div class="gallery-item" role="img" aria-label="Spray gun applying orange paint to a metal part" style="left:113px;top:476px;width:321px;height:253px;background:linear-gradient(120deg,#b6c0c7,#d27a3e 55%,#e76a1c)"></div>
  <div class="gallery-item" role="img" aria-label="Painter on a ladder decorating an interior wall" style="left:446px;top:476px;width:309px;height:253px;background:linear-gradient(135deg,#d7d6d1,#4c7770 55%,#8d7a5c)"></div>
  <div class="gallery-item" role="img" aria-label="Rope access painters working on a high-rise facade" style="left:766px;top:476px;width:321px;height:253px;background:linear-gradient(135deg,#e2e7ec,#aebdcc 60%,#8a9fb0)"></div>
</section>

<section class="team">
  <h2 class="section-title" style="top:70px;color:#fff">Our Team (Bio)</h2>
  <div class="title-rule" style="top:125px;background:#fff"></div>
  <div class="member" style="left:81px">
    <div class="member-photo"><div role="img" aria-label="Portrait of team member in plaid shirt" style="background:linear-gradient(160deg,#eee,#a9b3bd)"></div></div>
    <div class="member-name">Jhone Deo</div>
    <div class="member-bio">Lorem ipsum dolor consectetur<br>adipiscing elit sed do eiusmod</div>
  </div>
  <div class="member" style="left:339px">
    <div class="member-photo"><div role="img" aria-label="Portrait of team member holding paint supplies" style="background:linear-gradient(160deg,#f2f2f2,#b7a99a)"></div></div>
    <div class="member-name">Jhone Deo</div>
    <div class="member-bio">Lorem ipsum dolor consectetur<br>adipiscing elit sed do eiusmod</div>
  </div>
  <div class="member" style="left:599px">
    <div class="member-photo"><div role="img" aria-label="Portrait of team member in apron holding a roller" style="background:linear-gradient(160deg,#f4f4f4,#3a3d44)"></div></div>
    <div class="member-name">Jhone Deo</div>
    <div class="member-bio">Lorem ipsum dolor consectetur<br>adipiscing elit sed do eiusmod</div>
  </div>
  <div class="member" style="left:857px">
    <div class="member-photo"><div role="img" aria-label="Portrait of team member with a yellow paint roller" style="background:linear-gradient(160deg,#f4f4f4,#c33b3b 60%,#2b4a8f)"></div></div>
    <div class="member-name">Jhone Deo</div>
    <div class="member-bio">Lorem ipsum dolor consectetur<br>adipiscing elit sed do eiusmod</div>
  </div>
</section>

<section class="testimonials">
  <h2 class="section-title" style="top:75px">Happy Customers</h2>
  <div class="title-rule" style="top:131px"></div>
  <article class="review" style="left:153px">
    <div class="stars">★★★★★</div>
    <p class="review-text">Lorem ipsum dolor sit ameed consectetur adipiscing elitsed do eiusmod tempor incididunte uted labore et dolore magna aliquad Uted enim ad minim veniam.</p>
    <div class="review-name">Jhon Doe</div>
    <div class="review-quote">“</div>
    <div class="review-avatar" role="img" aria-label="Customer portrait"></div>
  </article>
  <article class="review" style="left:624px">
    <div class="stars">★★★★★</div>
    <p class="review-text">Lorem ipsum dolor sit ameed consectetur adipiscing elitsed do eiusmod tempor incididunte uted labore et dolore magna aliquad Uted enim ad minim veniam.</p>
    <div class="review-name">Jhon Doe</div>
    <div class="review-quote">“</div>
    <div class="review-avatar" role="img" aria-label="Customer portrait"></div>
  </article>
</section>

<footer class="site-footer">
  <div class="footer-col" style="left:110px">
    <h4>Quick Links</h4>
    <ul><li>Home</li><li>About</li><li>Services</li><li>Gallery</li><li>Team</li><li>Testimonoals</li><li>Contact Us</li></ul>
  </div>
  <div class="footer-col" style="left:302px">
    <h4>About Company</h4>
    <ul><li>Terms of Use</li><li>Terms &amp; Condition</li><li>News</li><li>Support</li><li>Contact Us</li><li>FAQ</li></ul>
  </div>
  <div class="footer-col" style="left:537px">
    <h4>Contact Us</h4>
    <div class="contact-item"><svg width="11" height="14" viewBox="0 0 12 16"><path d="M6 0a6 6 0 0 0-6 6c0 4.5 6 10 6 10s6-5.5 6-10a6 6 0 0 0-6-6zm0 8.5A2.5 2.5 0 1 1 6 3.5a2.5 2.5 0 0 1 0 5z" fill="var(--green)"/></svg><div><b>Location</b>241,Lorem ipsum dolor sited<br>Consectetur adipiscing elited</div></div>
    <div class="contact-item"><svg width="12" height="12" viewBox="0 0 24 24"><path d="M6.6 10.8a15 15 0 0 0 6.6 6.6l2.2-2.2a1 1 0 0 1 1-.25 11.4 11.4 0 0 0 3.6.57 1 1 0 0 1 1 1V20a1 1 0 0 1-1 1A17 17 0 0 1 3 4a1 1 0 0 1 1-1h3.5a1 1 0 0 1 1 1c0 1.25.2 2.45.57 3.57a1 1 0 0 1-.25 1z" fill="var(--green)"/></svg><div><b>Phone</b>+1 555 014 2270</div></div>
    <div class="contact-item"><svg width="12" height="10" viewBox="0 0 16 12"><rect width="16" height="12" rx="1" fill="var(--green)"/><path d="M0 1l8 6 8-6" stroke="#101212" stroke-width="1.4" fill="none"/></svg><div><b>Email</b>info@brookhollowpaintcontractors.com</div></div>
  </div>
  <div class="footer-col" style="left:855px">
    <h4>Stil have questios?</h4>
    <p class="footer-note">Contact us using this form. A repesenta-tive will aswer your questions as soon as possible.</p>
    <div class="footer-btn">GET A QUOTE</div>
  </div>
  <div class="to-top"><svg width="14" height="14" viewBox="0 0 14 14"><path d="M3 9l4-4 4 4" stroke="#fff" stroke-width="2" fill="none"/></svg></div>
  <div class="copyright">2023 Copyright -Brookhollow Paint Contractors, LLC &nbsp;| All Rights Reserved</div>
</footer>

</body>
</html>
```